Two companies with one (great) goal... Need a Business card Design

Our Design consists of 2 companies with a common goal-- Embracing a Healthy Lifestyle!
1. The Vitality & Health Travel Trust- consists of a large ranch where horses, and crops of plants and vegetables are a significant component. Tourism developments are underway and the Ffoundation plays a significant role in supporting Sporting events.
2. Pelvaro is a manufacturer of medical and diagnostic equipment inclusive of small medical outposts throughout remote and rural regions of the country.

We are looking for a 2 sided business card with one company on each side. The ideal design will make the 2 different businesses flow together, while at the same time, also work if only one side was printed.

Information for Pelvaro Design:
Medical, Diagnostic and Laboratory Equipment | Medical Imaging NimbusVault ScanHub | Biomedical Services
www.pelvaro-example.bz
info@pelvaro-example.bz
Tel: (555) 382) 9160

Information for The Vitality & Health Travel Trust:
DIRECTOR NAME
Belize, Central America
www.vitalitytrust-example.bz
info@vitalitytrust-example.bz
Tel: (555) 947-2813

*It is important that the font used is not too small please.

A few different color variations of each logo are included, any variation could be used.

Tagline is being finalized but ideally there would be a spot to add this in the future. Top tagline currently is "Healthy Lifestyle Through Better Living"

Industry/Entity Type

Medical

Requirements
Must have
• Font that is large enough to read

```html
<!DOCTYPE html>
<html lang="en">
<head>
<meta charset="utf-8">
<title>Business Cards</title>
<link rel="stylesheet" href="https://fonts.googleapis.com/css2?family=Open+Sans:wght@400;600;700&display=swap">
<style>
  :root {
    --page: #e9e9ee;
    --card: #ffffff;
    --ink: #3a3a3a;
    --muted: #5b5b5b;
    --blue: #1a7bc4;
    --green: #7ab940;
    --gold: #d49a3a;
    --gold-light: #f3d08a;
    --black: #111111;
    --rule: #b9b9b9;
  }
  html, body {
    margin: 0;
    width: 1200px;
    height: 987px;
    overflow: hidden;
    background: var(--page);
    font-family: "Open Sans", Arial, sans-serif;
    color: var(--ink);
  }
  .card {
    position: absolute;
    left: 210px;
    width: 780px;
    height: 446px;
    background: var(--card);
    border-radius: 22px;
    overflow: hidden;
    box-shadow: 0 6px 18px rgba(0,0,0,0.12);
  }
  .card--trust { top: 30px; }
  .card--pelvaro { top: 511px; }
  .card__art { position: absolute; inset: 0; }

  .brand {
    position: absolute;
    display: flex;
    align-items: center;
    gap: 22px;
  }
  .brand__name { margin: 0; line-height: 1; }
  .brand__mark { display: block; }

  .card--pelvaro .brand { left: 48px; top: 48px; }
  .card--pelvaro .brand__name {
    font-size: 92px; font-weight: 600; color: var(--blue); letter-spacing: 2px;
  }
  .card--pelvaro .brand__mark { width: 64px; height: 64px; background: var(--green); }

  .card--trust .brand { left: 48px; top: 40px; }
  .card--trust .brand__name {
    font-size: 34px; font-weight: 600; color: var(--gold); letter-spacing: 1px;
  }
  .card--trust .brand__mark { width: 40px; height: 40px; border-radius: 50%; background: var(--gold); }

  .tagline {
    position: absolute; left: 48px; top: 96px; margin: 0;
    font-size: 20px; font-weight: 700; color: var(--muted);
  }

  .details {
    position: absolute;
    display: flex;
    align-items: stretch;
    gap: 22px;
  }
  .card--pelvaro .details { left: 48px; top: 180px; }
  .card--trust .details { left: 48px; top: 150px; }

  .details__left { text-align: right; font-size: 20px; line-height: 1.45; color: var(--muted); }
  .details__left p { margin: 0; }
  .director { font-size: 24px; font-weight: 700; color: var(--ink); }

  .services { list-style: none; margin: 0; padding: 0; }
  .services li::before { content: "• "; }

  .divider { width: 2px; background: var(--rule); }

  .contacts { list-style: none; margin: 0; padding: 0; font-size: 22px; line-height: 1.6; color: var(--muted); }
  .contacts li { display: flex; align-items: center; gap: 10px; }
  .contacts svg { width: 20px; height: 20px; flex: none; }
</style>
</head>
<body>

<section class="card card--trust">
  <svg class="card__art" viewBox="0 0 780 446" preserveAspectRatio="none">
    <defs>
      <linearGradient id="goldSweep" x1="0" y1="0" x2="1" y2="0">
        <stop offset="0" stop-color="#c8882a"/>
        <stop offset="0.45" stop-color="#f3d08a"/>
        <stop offset="1" stop-color="#c8882a"/>
      </linearGradient>
    </defs>
    <path d="M0,270 C90,270 170,320 300,360 C440,400 600,400 780,360 L780,446 L0,446 Z" fill="#111111"/>
    <path d="M0,310 C110,300 190,345 320,380 C460,415 620,410 780,375 L780,446 L0,446 Z" fill="url(#goldSweep)"/>
  </svg>

  <div class="brand">
    <span class="brand__mark"></span>
    <h1 class="brand__name">The Vitality &amp; Health Travel Trust</h1>
  </div>
  <p class="tagline">Healthy Lifestyle Through Better Living</p>

  <div class="details">
    <div class="details__left">
      <p class="director">DIRECTOR NAME</p>
      <p>Belize, Central America</p>
    </div>
    <span class="divider"></span>
    <ul class="contacts">
      <li>
        <svg viewBox="0 0 20 20"><circle cx="10" cy="10" r="9" fill="none" stroke="#d49a3a" stroke-width="2"/><path d="M7 5l2 3-1 1c1 2 2 3 4 4l1-1 3 2-1 2c-5 0-10-5-10-10z" fill="#d49a3a"/></svg>
        (555) 947-2813
      </li>
      <li>
        <svg viewBox="0 0 20 20"><rect x="2" y="5" width="16" height="11" rx="1" fill="#d49a3a"/><path d="M2 5l8 6 8-6" fill="none" stroke="#fff" stroke-width="1.5"/></svg>
        name@vitalitytrust-example.bz
      </li>
      <li>
        <svg viewBox="0 0 20 20"><circle cx="10" cy="10" r="8" fill="none" stroke="#d49a3a" stroke-width="2"/><path d="M2 10h16M10 2c-4 4-4 12 0 16M10 2c4 4 4 12 0 16" fill="none" stroke="#d49a3a" stroke-width="1.5"/></svg>
        www.vitalitytrust-example.bz
      </li>
    </ul>
  </div>
</section>

<section class="card card--pelvaro">
  <svg class="card__art" viewBox="0 0 780 446" preserveAspectRatio="none">
    <path d="M0,215 C60,360 300,440 620,446" fill="none" stroke="#7ab940" stroke-width="10"/>
    <path d="M0,250 C70,380 300,446 570,446 L0,446 Z" fill="#1a7bc4"/>
  </svg>

  <div class="brand">
    <h1 class="brand__name">PELVARO</h1>
    <span class="brand__mark"></span>
  </div>

  <div class="details">
    <div class="details__left">
      <ul class="services">
        <li>Medical</li>
        <li>Diagnostic and Laboratory Equipment</li>
        <li>Medical Imaging NimbusVault ScanHub</li>
        <li>Biomedica Services</li>
      </ul>
    </div>
    <span class="divider"></span>
    <ul class="contacts">
      <li>
        <svg viewBox="0 0 20 20"><circle cx="10" cy="10" r="9" fill="none" stroke="#1a7bc4" stroke-width="2"/><path d="M7 5l2 3-1 1c1 2 2 3 4 4l1-1 3 2-1 2c-5 0-10-5-10-10z" fill="#1a7bc4"/></svg>
        (555) 382) 9160
      </li>
      <li>
        <svg viewBox="0 0 20 20"><rect x="2" y="5" width="16" height="11" rx="1" fill="#1a7bc4"/><path d="M2 5l8 6 8-6" fill="none" stroke="#fff" stroke-width="1.5"/></svg>
        name@pelvaro-example.bz
      </li>
      <li>
        <svg viewBox="0 0 20 20"><circle cx="10" cy="10" r="8" fill="none" stroke="#1a7bc4" stroke-width="2"/><path d="M2 10h16M10 2c-4 4-4 12 0 16M10 2c4 4 4 12 0 16" fill="none" stroke="#1a7bc4" stroke-width="1.5"/></svg>
        www.pelvaro-example.bz
      </li>
    </ul>
  </div>
</section>

</body>
</html>
```